Business card design needed with water logo.

I have already designed a card at Cardlyne, but prepared to pay $139 as advertised for a more professional look.
I presume it will then be available to me to order through Card Lyne?
The Website address needs to be large font.
I sell light weight water features at shopping centres to the public but at wholesale prices.
Need a card that is EASY TO READ, as go through literally thousands of cards as customer pick them up from my display stand.
The current logo I use is the Card Lyne Pebblemark.
PLEASE PLACE ALL INFORMATION THAT I HAVE PROVIDED ON THE CARD
Designers keep missing out my requirements

Target Market(s)

Retail prospective customers who walk by and take a card for future reference. I go through thousands of cards so economical is a must

Industry/Entity Type

Shopping

Contact Information for Business Card

StoneFlow Company
W.A. Wholesale Agent for Rockspouts QLD
Light Weight Fibre Glass Water Features
www.rockspoutsonline.com.au
See website for products but listed are RETAIL Prices
contact
MAREN TOWSLEY
for WA Wholesale Direct Pricing
Ph: 0428596317 email: stoneflowco@brinkmail.net.au

BACK OF CARD to Read.
Stoneflow Company DISPLAYS ONLY AT SHOPPING CENTRES
..........................................................................
.........................................................................
WAREHOUSE STORAGE ONLY ( No Display)
KESTRELWAY FREIGHT
14 Pardoe Rd, Kewdale WA 6105 ABN 58209364172

Logo Text

StoneFlow Company

Logo styles of interest
Pictorial/Combination Logo
Requirements
Must have
• Large font to be easy to read, ALL INFORMATION On, that I specified.
This information is from my own designed card and I require the same Information just in a more professional format.

```html
<!DOCTYPE html>
<html lang="en">
<head>
<meta charset="utf-8">
<title>StoneFlow Company Business Card</title>
<link rel="stylesheet" href="https://fonts.googleapis.com/css2?family=Barlow:wght@300;400;700;800;900&display=swap">
<style>
  :root {
    --brand-blue: #0ba7e4;
    --ink: #3b4a52;
    --ink-light: #5c6a71;
    --muted: #a7b0b4;
    --frame: #4a4f53;
    --rule-fill: #eceeed;
    --paper: #ffffff;
  }
  * { margin: 0; padding: 0; box-sizing: border-box; }
  html, body { width: 1200px; height: 800px; overflow: hidden; background: var(--paper); }
  body { font-family: "Barlow", Arial, sans-serif; color: var(--ink); position: relative; }

  .card {
    position: absolute; top: 298px; width: 471px; height: 266px;
    border: 1.5px solid var(--frame); background: var(--paper);
  }
  .card--front { left: 103px; }
  .card--back { left: 626px; }

  .wordmark {
    position: absolute; left: 18px; top: 18px;
    font-weight: 900; font-size: 46px; line-height: 36px;
    color: var(--brand-blue); letter-spacing: 0.2px;
  }
  .mark-dot {
    position: absolute; left: 380px; top: 48px; width: 60px; height: 60px;
    border-radius: 50%; background: var(--brand-blue);
  }
  .agent-lines {
    position: absolute; left: 20px; top: 103px;
    font-weight: 400; font-size: 14px; line-height: 15.5px; color: var(--brand-blue);
  }
  .pricing {
    position: absolute; left: 20px; top: 149px;
    font-size: 15px; line-height: 15.5px; color: var(--ink-light); font-weight: 300;
  }
  .pricing .web { font-weight: 800; color: var(--ink); }
  .contact-tag {
    position: absolute; left: 20px; height: 21px; padding: 0 6px;
    background: var(--ink); color: var(--paper);
    font-weight: 800; font-size: 15px; line-height: 21px; letter-spacing: 0.2px;
  }
  .contact-tag--name { top: 198px; }
  .contact-tag--email { top: 222px; letter-spacing: 0.6px; }

  .back-info {
    position: absolute; left: 24px; top: 19px;
    font-size: 15px; line-height: 16.2px; color: var(--ink-light); font-weight: 300;
  }
  .back-info .accent { color: var(--brand-blue); font-weight: 800; }
  .back-info .strong { color: var(--ink); font-weight: 800; }
  .back-info .note { color: var(--muted); font-weight: 300; }

  .writing-rules { position: absolute; left: 25px; top: 134px; width: 419px; list-style: none; }
  .writing-rules li { height: 16px; margin-bottom: 2.6px; background: var(--rule-fill); }
</style>
</head>
<body>
  <section class="card card--front" aria-label="Card front">
    <h1 class="wordmark">STONEFLOW<br>COMPANY</h1>
    <div class="mark-dot" aria-hidden="true"></div>
    <p class="agent-lines">W.A. WHOLESALE AGENT FOR ROCKSPOUTS<br>QLD LIGHT WEIGHT FIBRE GLASS WATER FEATURES</p>
    <p class="pricing">SEE WEBSITE FOR PRODUCTS BUT LISTED ARE RETAIL PRICES<br><span class="web">WWW.ROCKSPOUTSONLINE.COM.AU</span><br>FOR W.A. WHOLESALE DIRECT PRICING</p>
    <p class="contact-tag contact-tag--name">MAREN TOWSLEY&nbsp; PH 0428596317</p>
    <p class="contact-tag contact-tag--email">STONEFLOWCO@BRINKMAIL.NET.AU</p>
  </section>

  <section class="card card--back" aria-label="Card back">
    <p class="back-info">
      <span class="accent">STONEFLOW COMPANY</span><br>
      <span class="accent">DISPLAYS ONLY AT SHOPPING CENTRES</span><br>
      <span class="strong">WAREHOUSE STORAGE ONLY</span> <span class="note">NO DISPLAY</span><br>
      <span class="strong">KESTRELWAY FREIGHT</span><br>
      14 PARDOE RD, BRANWICK WA 6112<br>
      <span class="strong">ABN 58209364172</span>
    </p>
    <ul class="writing-rules" aria-label="Lines for notes">
      <li></li><li></li><li></li><li></li><li></li><li></li>
    </ul>
  </section>
</body>
</html>
```